Attractive Flyer for Moving Company

Our Company is called "Harborline Haulers".
We provide moving service for home and businesses
We need a flyer for a moving company, located in South Florida USA
Flyer size will be 7 x 5 inches, double sided.

Flyer needs to be very attractive and catchy for eye. I want people to keep it even if they don't need our service. I attached a lot of text in separate word file.
Logo, brief and additional pictures are attached.

```html
<!DOCTYPE html>
<html lang="en">
<head>
<meta charset="utf-8">
<title>Harborline Haulers – Special Deal Flyer</title>
<link rel="stylesheet" href="https://fonts.googleapis.com/css2?family=Oswald:wght@400;500;600&family=Roboto+Condensed:ital,wght@0,700;1,800&display=swap">
<style>
  :root {
    --backdrop: #e9ebee;
    --paper: #ffffff;
    --ink: #111111;
    --brand-red: #e3141b;
  }
  * { margin: 0; padding: 0; box-sizing: border-box; }
  html, body { width: 1200px; height: 1200px; overflow: hidden; }
  body {
    background: var(--backdrop);
    display: flex;
    align-items: center;
    justify-content: center;
  }
  .flyer {
    position: relative;
    width: 1140px;
    height: 640px;
    background: var(--paper);
    box-shadow: 0 4px 18px rgba(0,0,0,0.15);
    padding: 34px 44px 36px 44px;
    color: var(--ink);
  }
  .voucher-note {
    position: absolute;
    top: 26px;
    right: 40px;
    font-family: "Oswald", sans-serif;
    font-weight: 500;
    font-size: 28px;
    color: var(--brand-red);
    letter-spacing: 0.2px;
  }
  .brand {
    display: flex;
    align-items: center;
    gap: 14px;
    margin-top: 62px;
  }
  .brand-dot {
    width: 34px;
    height: 34px;
    border-radius: 50%;
    background: var(--brand-red);
  }
  .brand-name {
    font-family: "Roboto Condensed", sans-serif;
    font-weight: 700;
    font-size: 48px;
    color: var(--brand-red);
    text-transform: uppercase;
    letter-spacing: 0.5px;
  }
  .deal-title {
    margin-top: 18px;
    display: flex;
    align-items: baseline;
    gap: 14px;
  }
  .deal-title .headline {
    font-family: "Roboto Condensed", sans-serif;
    font-style: italic;
    font-weight: 800;
    font-size: 58px;
    line-height: 1;
  }
  .deal-title .restriction {
    font-family: "Oswald", sans-serif;
    font-weight: 500;
    font-size: 32px;
    color: var(--brand-red);
  }
  .savings {
    font-family: "Roboto Condensed", sans-serif;
    font-style: italic;
    font-weight: 800;
    font-size: 52px;
    line-height: 1.05;
    margin-top: 4px;
  }
  .offer-list {
    list-style: none;
    font-family: "Oswald", sans-serif;
    font-weight: 500;
    font-size: 34px;
    line-height: 1.22;
    margin-top: 4px;
  }
  .included {
    margin-top: 16px;
    font-family: "Oswald", sans-serif;
    font-weight: 400;
    font-size: 30px;
    line-height: 1.2;
    text-transform: uppercase;
    letter-spacing: 0.3px;
  }
  .included ul { list-style: none; }
  .included li::before { content: "- "; }
</style>
</head>
<body>
  <main class="flyer">
    <p class="voucher-note">Keep this voucher, it is valid until January 1st, 2020</p>

    <header class="brand">
      <span class="brand-dot"></span>
      <span class="brand-name">Harborline Haulers</span>
    </header>

    <div class="deal-title">
      <h1 class="headline">Your Special Deal</h1>
      <span class="restriction">(Cannot be used with another promotions or coupons)</span>
    </div>
    <p class="savings">SAVE 15% -25% on your move</p>

    <ul class="offer-list">
      <li>$275 – 3 hours of Moving Service with 2 PRO MOVERS</li>
      <li>$325 - 3 hours of Moving Service with 3 PRO MOVERS</li>
      <li>+ 20% OFF boxes and packing supplies.</li>
    </ul>

    <section class="included">
      <h2 class="included-title" style="font-weight:400;font-size:30px;">Included in price</h2>
      <ul>
        <li>Protection of your furniture with specialized blankets and plastic wrap.</li>
        <li>Disassembly and reassembly of your furniture.</li>
        <li>Wardrobe boxes for the duration of moving process.</li>
      </ul>
    </section>
  </main>
</body>
</html>
```